Front & Back Book Cover Design

Title:
THE QUIET LANDLORD: How to Grow Comfort and Capital Through Property You Merely Guide
Author:
Wes T. Marlund
Design Philosophy:
A modern, minimalist-luxury aesthetic that feels visionary and intelligent — positioned between business innovation (The Nimble Venture), modern finance (The Temperament of Wealth), and timeless real estate insight (Bold Uncle Meek Uncle).
Think: clean, bold, and idea-driven — a visual reflection of the book’s central concept: wealth through clarity, not clutter.
Back Cover:
To include book description along with author photo and bio
Files:
PNG, PDF, EPUB

```html
<!DOCTYPE html>
<html lang="en">
<head>
<meta charset="utf-8">
<title>The Quiet Landlord — Front Cover</title>
<link rel="stylesheet" href="https://fonts.googleapis.com/css2?family=Jost:wght@400;500&family=Quicksand:wght@500;600&display=swap">
<style>
  :root {
    --stage: #ece8e1;
    --cover: #2b2f36;
    --cover-glow: #33414a;
    --gold-light: #f3e3b8;
    --gold: #e0b45a;
    --gold-deep: #c98d1f;
    --frame: #7fe6e8;
    --frame-fill-1: #16343a;
    --frame-fill-2: #0e1d22;
    --ink-light: #f4f4f2;
  }
  * { box-sizing: border-box; margin: 0; padding: 0; }
  html, body {
    width: 1200px; height: 730px; overflow: hidden;
    background: var(--stage);
  }
  .stage {
    width: 1200px; height: 730px;
    display: flex; align-items: center; justify-content: center;
  }
  .cover {
    position: relative;
    width: 460px; height: 690px;
    background: radial-gradient(ellipse 55% 35% at 50% 50%, var(--cover-glow) 0%, var(--cover) 70%);
    box-shadow: 0 10px 30px rgba(0,0,0,0.18);
    text-align: center;
    color: var(--ink-light);
  }
  .cover-title {
    position: absolute; top: 58px; left: 0; right: 0;
    font-family: "Jost", sans-serif; font-weight: 400;
    line-height: 0.92;
  }
  .cover-title span {
    display: block;
    background: linear-gradient(100deg, var(--gold-light) 0%, var(--gold) 45%, var(--gold-deep) 100%);
    -webkit-background-clip: text; background-clip: text;
    color: transparent;
  }
  .title-lead { font-size: 34px; letter-spacing: 2px; margin-bottom: 8px; }
  .title-main { font-size: 76px; letter-spacing: 1px; }
  .cover-art {
    position: absolute; top: 262px; left: 50%;
    width: 104px; height: 186px; margin-left: -52px;
    background: linear-gradient(160deg, var(--frame-fill-1), var(--frame-fill-2));
    border: 3px solid var(--frame);
    box-shadow: 0 0 14px rgba(127,230,232,0.7), 0 0 60px rgba(127,230,232,0.25), inset 0 0 12px rgba(127,230,232,0.4);
  }
  .cover-subtitle {
    position: absolute; top: 488px; left: 0; right: 0;
    font-family: "Quicksand", sans-serif; font-weight: 500;
    font-size: 17px; line-height: 1.35; letter-spacing: 0.3px;
  }
  .cover-author {
    position: absolute; top: 600px; left: 0; right: 0;
    font-family: "Quicksand", sans-serif; font-weight: 600;
    font-size: 28px; letter-spacing: 0.5px;
  }
</style>
</head>
<body>
<main class="stage">
  <section class="cover">
    <h1 class="cover-title">
      <span class="title-lead">THE</span>
      <span class="title-main">QUIET</span>
      <span class="title-main">LANDLORD</span>
    </h1>
    <div class="cover-art" role="img" aria-label="Glowing teal frame holding an abstract network of gold and teal property lines"></div>
    <p class="cover-subtitle">How to Grow Comfort and Capital<br>Through Property You Merely Guide</p>
    <p class="cover-author">Wes T. Marlund</p>
  </section>
</main>
</body>
</html>
```